24 Hour Fitness Center Store front. Window advertisment

We need a signage design for a 24 hour fitness center in Central FL. Bright Peak Fitness. I have attached photos that show our store front. The signage will cover 4 windows from the far left side towards the right, and 3 windows from the far right towards the left. So 7 windows total. The middle windows including the doors will be blank for customers to see inside.
We want to portray "Results" when people walk up. Our colors are shown on our Logo (attached). Red, gray, black. We are open to any ideas and concepts as far as how the layout is shown, example: Each window a different image, or one large image on each side shown through all windows. I have also attached some examples of other stores that look appealing. Our Services include 24 hour access, personal training, tanning, and group exercise. Each window is approximately 60 inches wide and 75 inches tall.
Thank you!
Fitness

```html
<!DOCTYPE html>
<html lang="en">
<head>
<meta charset="utf-8">
<title>Bright Peak Fitness – Window Signage</title>
<link href="https://fonts.googleapis.com/css2?family=Roboto+Condensed:wght@400;700&display=swap" rel="stylesheet">
<style>
  :root {
    --brand-red: #dc2a1f;
    --ink: #2b2b2b;
    --paper: #ffffff;
    --board-line: #c9c9c9;
    --panel-line: #1e1e1e;
  }
  html, body {
    margin: 0;
    width: 1200px;
    height: 733px;
    overflow: hidden;
    background: var(--paper);
    font-family: "Roboto Condensed", sans-serif;
  }
  .board {
    position: absolute;
    left: 9px; top: 9px;
    width: 1178px; height: 705px;
    border: 1px solid var(--board-line);
    box-shadow: 3px 3px 4px rgba(0,0,0,.25);
    background: var(--paper);
  }
  .window {
    position: absolute;
    border: 1px solid var(--panel-line);
    background: var(--paper);
    box-sizing: border-box;
  }
  .window svg { display: block; width: 100%; height: 100%; }
  .window--large { top: 32px; width: 370px; height: 462px; }
  .window--small { top: 503px; width: 158px; height: 196px; }
  .letter, .side-block { fill: var(--brand-red); }
  .letter-stroke { fill: none; stroke: var(--brand-red); stroke-width: 46; }
  .services {
    font-family: "Roboto Condensed", sans-serif;
    font-weight: 700;
    font-size: 13.4px;
    fill: var(--ink);
  }
  .brand-name {
    font-family: "Roboto Condensed", sans-serif;
    font-weight: 700;
    font-size: 11px;
    fill: var(--ink);
  }
  .brand-dot { fill: var(--brand-red); }
</style>
</head>
<body>
<svg width="0" height="0" style="position:absolute" aria-hidden="true">
  <defs>
    <linearGradient id="tone-warm" x1="0" y1="0" x2="1" y2="1">
      <stop offset="0" stop-color="#9cc3d8"/><stop offset=".5" stop-color="#d9a58c"/><stop offset="1" stop-color="#2f8f8a"/>
    </linearGradient>
    <linearGradient id="tone-gym" x1="0" y1="0" x2="1" y2="1">
      <stop offset="0" stop-color="#d8dde0"/><stop offset=".5" stop-color="#6f6a68"/><stop offset="1" stop-color="#c9c4c8"/>
    </linearGradient>
    <linearGradient id="tone-cycle" x1="0" y1="0" x2="1" y2="1">
      <stop offset="0" stop-color="#e6e6e6"/><stop offset=".5" stop-color="#b58f78"/><stop offset="1" stop-color="#3c3f44"/>
    </linearGradient>
    <linearGradient id="tone-blue" x1="0" y1="0" x2="1" y2="1">
      <stop offset="0" stop-color="#3a8fd0"/><stop offset=".5" stop-color="#d29a7c"/><stop offset="1" stop-color="#2b2b2b"/>
    </linearGradient>
    <linearGradient id="tone-pink" x1="0" y1="0" x2="1" y2="1">
      <stop offset="0" stop-color="#cfe0e8"/><stop offset=".5" stop-color="#d779a6"/><stop offset="1" stop-color="#6a5a8a"/>
    </linearGradient>
    <linearGradient id="tone-dark" x1="0" y1="0" x2="1" y2="1">
      <stop offset="0" stop-color="#e8ecef"/><stop offset=".5" stop-color="#2a2f3a"/><stop offset="1" stop-color="#b9bfc6"/>
    </linearGradient>

    <path id="glyph-r" class="letter" fill-rule="evenodd"
      d="M140 116 H285 C335 116 355 145 355 180 C355 212 335 232 305 238 L369 345 H300 L245 245 H200 V345 H140 Z
         M200 160 H275 C295 160 300 170 300 182 C300 195 292 205 275 205 H200 Z"/>
    <path id="glyph-e" class="letter"
      d="M60 116 H360 V165 H130 V205 H330 V255 H130 V295 H360 V345 H60 Z"/>
    <path id="glyph-s" class="letter-stroke"
      d="M335 175 C315 145 265 139 185 139 C90 139 47 158 47 185 C47 215 100 225 185 230 C275 235 322 248 322 278 C322 308 275 322 185 322 C100 322 55 310 35 282"/>
    <path id="glyph-u" class="letter"
      d="M40 116 H120 V255 C120 280 150 290 185 290 C220 290 250 280 250 255 V116 H330 V255 C330 320 270 345 185 345 C100 345 40 320 40 255 Z"/>
    <path id="glyph-l" class="letter"
      d="M60 116 H140 V285 H350 V345 H60 Z"/>
    <path id="glyph-t" class="letter"
      d="M40 116 H340 V170 H225 V345 H155 V170 H40 Z"/>

    <g id="window-footer">
      <text class="services" x="184.5" y="361" text-anchor="middle" textLength="355" lengthAdjust="spacingAndGlyphs">24 Hour Access | Personal Training | Tanning | Group Exercise</text>
      <circle class="brand-dot" cx="262" cy="424" r="4"/>
      <text class="brand-name" x="270" y="428">Bright Peak Fitness</text>
    </g>
  </defs>
</svg>

<div class="board"></div>

<!-- Large windows -->
<div class="window window--large" style="left:27px">
  <svg viewBox="0 0 369 461">
    <rect class="side-block" x="0" y="116" width="60" height="229"/>
    <rect x="60" y="116" width="240" height="229" fill="url(#tone-warm)" role="img" aria-label="Photo: women riding exercise bikes in a spin class"/>
    <use href="#glyph-r"/>
    <use href="#window-footer"/>
  </svg>
</div>
<div class="window window--large" style="left:412px">
  <svg viewBox="0 0 369 461">
    <rect class="side-block" x="0" y="116" width="60" height="229"/>
    <rect x="60" y="116" width="240" height="229" fill="url(#tone-gym)" role="img" aria-label="Photo: man lifting a dumbbell beside a smiling woman in a gym"/>
    <use href="#glyph-e"/>
    <use href="#window-footer"/>
  </svg>
</div>
<div class="window window--large" style="left:796px">
  <svg viewBox="0 0 369 461">
    <rect x="85" y="116" width="210" height="230" fill="url(#tone-cycle)" role="img" aria-label="Photo: group cycling class in a row of bikes"/>
    <use href="#glyph-s"/>
    <use href="#window-footer"/>
  </svg>
</div>

<!-- Full RESULTS window run -->
<div class="window window--small" style="left:27px">
  <svg viewBox="0 0 369 461">
    <rect class="side-block" x="0" y="116" width="60" height="229"/>
    <rect x="60" y="116" width="240" height="229" fill="url(#tone-warm)" role="img" aria-label="Photo: women riding exercise bikes in a spin class"/>
    <use href="#glyph-r"/>
    <use href="#window-footer"/>
  </svg>
</div>
<div class="window window--small" style="left:191px">
  <svg viewBox="0 0 369 461">
    <rect class="side-block" x="0" y="116" width="60" height="229"/>
    <rect x="60" y="116" width="240" height="229" fill="url(#tone-gym)" role="img" aria-label="Photo: man lifting a dumbbell beside a smiling woman in a gym"/>
    <use href="#glyph-e"/>
    <use href="#window-footer"/>
  </svg>
</div>
<div class="window window--small" style="left:355px">
  <svg viewBox="0 0 369 461">
    <rect x="85" y="116" width="210" height="230" fill="url(#tone-cycle)" role="img" aria-label="Photo: group cycling class in a row of bikes"/>
    <use href="#glyph-s"/>
    <use href="#window-footer"/>
  </svg>
</div>
<div class="window window--small" style="left:518px">
  <svg viewBox="0 0 369 461">
    <rect class="side-block" x="0" y="116" width="40" height="229"/>
    <rect x="40" y="116" width="290" height="229" fill="url(#tone-blue)" role="img" aria-label="Photo: man doing push-ups on kettlebells"/>
    <use href="#glyph-u"/>
    <use href="#window-footer"/>
  </svg>
</div>
<div class="window window--small" style="left:682px">
  <svg viewBox="0 0 369 461">
    <rect class="side-block" x="0" y="116" width="60" height="229"/>
    <rect x="60" y="116" width="240" height="229" fill="url(#tone-cycle)" role="img" aria-label="Photo: woman on a spin bike in a cycling class"/>
    <use href="#glyph-l"/>
    <use href="#window-footer"/>
  </svg>
</div>
<div class="window window--small" style="left:845px">
  <svg viewBox="0 0 369 461">
    <rect class="side-block" x="0" y="116" width="40" height="229"/>
    <rect x="40" y="116" width="270" height="229" fill="url(#tone-pink)" role="img" aria-label="Photo: two women smiling in workout clothes"/>
    <use href="#glyph-t"/>
    <use href="#window-footer"/>
  </svg>
</div>
<div class="window window--small" style="left:1009px">
  <svg viewBox="0 0 369 461">
    <rect x="85" y="116" width="210" height="230" fill="url(#tone-dark)" role="img" aria-label="Photo: man in a sleeveless shirt training in a gym"/>
    <use href="#glyph-s"/>
    <use href="#window-footer"/>
  </svg>
</div>
</body>
</html>
```